TerraLume Business Card Design Project

We need a business card design for a new company called "TerraLume Systems". TerraLume provides 3D visualization software for subsurface oil and gas data so you can make confident downhole decisions.

Our goal is to provide easy to understand big pictures of your data so your can make confident planning decisions.

Our tagline is
SEAMLESS DATA SHARING. EFFECTIVE COLLABORATION. CONFIDENT DECISION-MAKING

Check out http://www.terralume-example.com for more ideas.

The design should promote a technology company that delivers web-based solutions focused on photo-realistic 3D graphics.

The colors from our existing logo (attached) are one option but not a requirement. The design SHOULD NOT use the existing logo.

The design should be two sided and full color. If you require any special print considerations (example: paper type, matte finish, metallic ink, etc) please provide detailed comments. Please also specify any desired details such as rounding of corners, etc.

IF YOU USE BLACK our printer states "We recommend using CMYK black (0, 0, 0, 100) or for a rich black (60, 40, 40, 100). Ensure your artwork is in CMYK mode before adjusting the black."

For design purposes you can use the following contact information

name: Harlan Pike
title: founder
phone: 555.987.6543
email: harlan@terralume-example.com

company information
TerraLume is our "branded" name
"TerraLume Systems" is our official name
www.terralume-example.com

address:
Suite 720
482 Birchmont Avenue SW
Calgary, AB, Canada
T3K 4R8

Target Market(s)

Companies spend a lot of time collecting, organizing and analyzing data but it's really hard to to get a big picture view of current and planned projects, especially in context to existing wellbores, geology and downhole equipment

TerraLume enables you to explore the big picture in an immersive, 3D environment. Our goal is to help transform you rich data into an easily understood picture, to make confident planning decisions and anticipate trouble events before the expensive execution phase.

Industry/Entity Type

Oil And Gas

Requirements
Must have
• The business card design should be sized to a standard 3.5 x 2 inches and print ready. See the attachment for a sample sized card
It MUST meet these requirements:
Exported as PDF file with two pages:
page 1: front design
page 2: back design
All Images must be 300ppi or higher (at 100%)
CMYK colour mode
0.125 inches of bleed on all sides (0.25 inches additional width and height)
0.125 inch safety margin (inside trim line)

```html
<!DOCTYPE html>
<html lang="en">
<head>
<meta charset="utf-8">
<title>TerraLume Systems – Business Card</title>
<link rel="stylesheet" href="https://fonts.googleapis.com/css2?family=Jost:wght@400;500&family=Archivo+Black&display=swap">
<style>
  :root {
    --page-bg: #eceeee;
    --card-white: #ffffff;
    --brand-green: #7ab648;
    --green-deep: #5f9a2c;
    --crimson: #9b1b3c;
    --crimson-shade: #5e0f24;
    --decor-grey: #eef0f0;
    --room-light: #f4f4f4;
    --room-mid: #d2d2d2;
    --room-dark: #a8a8a8;
  }
  * { margin: 0; padding: 0; box-sizing: border-box; }
  html, body {
    width: 1200px; height: 702px; overflow: hidden;
    background: var(--page-bg);
  }
  .sheet {
    position: relative; width: 1200px; height: 702px;
    display: flex; align-items: center; justify-content: center; gap: 60px;
  }
  .card {
    position: relative; width: 520px; height: 297px; overflow: hidden;
    box-shadow: 0 10px 28px rgba(0,0,0,0.18);
  }

  /* Front */
  .card-front { background: var(--card-white); font-family: "Jost", sans-serif; color: var(--brand-green); }
  .wireframe-area {
    position: absolute; left: 40px; top: 60px; width: 380px; height: 170px;
    background: linear-gradient(160deg, var(--card-white) 0%, var(--decor-grey) 50%, var(--card-white) 100%);
  }
  .brand {
    position: absolute; left: 24px; top: 24px;
    display: flex; align-items: center; gap: 8px;
    font-size: 19px; font-weight: 500; color: var(--brand-green);
  }
  .brand-mark { width: 14px; height: 14px; background: var(--brand-green); }
  .person { position: absolute; left: 180px; top: 104px; text-align: left; }
  .person-name { font-size: 32px; font-weight: 400; line-height: 1; }
  .person-title { font-size: 20px; font-weight: 400; margin-top: 4px; padding-left: 48px; }
  .contact { position: absolute; left: 24px; bottom: 22px; font-size: 13px; line-height: 1.55; }
  .contact .web { font-size: 18px; line-height: 1.35; }
  .address { position: absolute; right: 22px; bottom: 26px; font-size: 13px; line-height: 1.5; }

  /* Back */
  .card-back { background: var(--room-mid); }
  .scene-area {
    position: absolute; inset: 0;
    background: radial-gradient(ellipse at 45% 45%, var(--room-light) 0%, var(--room-mid) 65%, var(--room-dark) 100%);
  }
  .headline {
    position: absolute; left: 60px; top: 62px; width: 290px; text-align: center;
    font-family: "Archivo Black", sans-serif; font-weight: 400; line-height: 1;
  }
  .headline .line-one, .headline .line-three {
    display: block; color: var(--crimson); font-size: 28px;
    text-shadow: 2px 2px 0 var(--crimson-shade);
  }
  .headline .line-two {
    display: block; color: var(--brand-green); font-size: 44px; margin: 8px 0 6px;
    text-shadow: 2px 2px 0 var(--green-deep);
  }
</style>
</head>
<body>
<main class="sheet">

  <section class="card card-front" aria-label="Card front">
    <div class="wireframe-area" role="img" aria-label="Faint wireframe 3D pipe model in the background"></div>
    <div class="brand"><span class="brand-mark"></span>TerraLume</div>
    <div class="person">
      <p class="person-name">Harlan Pike</p>
      <p class="person-title">founder</p>
    </div>
    <div class="contact">
      <p>Phone: (555) 987-6543</p>
      <p>Email: harlan@terralume-example.com</p>
      <p class="web">www.terralume-example.com</p>
    </div>
    <div class="address">
      <p>Suite 720 482 Birchmont Avenue SW</p>
      <p>Calgary, AB, Canada T3K 4R8</p>
    </div>
  </section>

  <section class="card card-back" aria-label="Card back">
    <div class="scene-area" role="img" aria-label="Rendered 3D room interior with a wireframe model of a pair of cylinders"></div>
    <h1 class="headline">
      <span class="line-one">Photo-realistic</span>
      <span class="line-two">3D</span>
      <span class="line-three">Graphics</span>
    </h1>
  </section>

</main>
</body>
</html>
```